Creating a page for our Spanish tutoring service

We recently launched a new service and would like to create new "solutions" pages to add to our website.

Previously, we provided private one-on-one Spanish tutoring. Now, we are also providing group classes.

We have two documents with some basic copy on each offering. Our website is nice and does not require changes currently, but we do not have the internal bandwidth to build these pages. You would be using our existing design elements to build these two web pages.

Repurposing/copying blocks from our other pages is fine! We have a developer, so design only is required. If you do a good job on this first project, we will have many more pages and projects for you to do!

Our website is lingotrail.com. TIA for any applicants.

---

Private classes copy:
https://files.quorvant.net/doc/7KqP2mZx9Lr4Wn8Tb3Vy6Hs1Jd5Fc0Ng/view

Group classes copy:
https://files.quorvant.net/doc/3Rb8Yt6Km1Xp9Qz4Ls7Gv2Nc5Wh0Dj8E/view

Target Market(s)

Online Spanish tutoring and online Spanish classes. We are a very high quality, yet affordable service. Our unique selling proposition is that we operate a completely remote team.

Current customers are typically well-to-do parents or professionals who want to learn Spanish for fun or personal development. They are usually in an okay standing financially (or want to be).

Those who pay for their kids to take lessons want them to have a better future or communicate with their families. Those who are young typically subscribe because they want a better future for themselves. Those who are 30+ years old learn for leisure, travel, or for ongoing professional development.

They want a quality product without paying the high costs associated with in-person tutoring, which is significantly more expensive. They also want to avoid cheaper solutions that are low cost but conversely low quality.

Number of Pages Required

2 page

Font styles to use
Other font styles liked:
• Avenir is our font

Requirements
Must have
• A look and feel consistent with the rest of our website.

```html
<!DOCTYPE html>
<html lang="en">
<head>
<meta charset="utf-8">
<title>LingoTrail – Private Tutoring and Group Classes</title>
<link rel="stylesheet" href="https://fonts.googleapis.com/css2?family=Poppins:wght@400;500;600;700&family=Montserrat:wght@400;500&display=swap">
<style>
:root{
  --backdrop:#c9e9e6;
  --teal:#53b5aa;
  --teal-deep:#3fa398;
  --orange:#f47c3f;
  --orange-deep:#e8652b;
  --ink:#3d4148;
  --muted:#6b7077;
  --mist:#f3f7f8;
  --sand:#f7f2ef;
  --press:#9ea2a7;
  --white:#ffffff;
}
*{box-sizing:border-box;margin:0;padding:0}
html,body{width:801px;height:1200px;overflow:hidden}
body{background:var(--backdrop);font-family:"Poppins",sans-serif;color:var(--ink)}
.stage{position:absolute;left:7px;top:0;width:1238px;height:1887px;transform:scale(.6359);transform-origin:0 0}
.page{position:absolute;top:0;width:582px;height:1887px;background:var(--white);overflow:hidden;box-shadow:0 4px 14px rgba(40,90,85,.18)}
.page--private{left:0}
.page--group{left:656px}
.section{position:absolute;left:0;width:582px}
.abs{position:absolute}

/* hero */
.hero{top:0;height:310px;background:var(--teal);color:var(--white)}
.brand{position:absolute;display:flex;align-items:center;gap:4px;font-weight:600;font-size:8px;letter-spacing:.3px}
.brand__mark{width:7px;height:7px;background:var(--white);border-radius:1px}
.hero .brand{left:43px;top:18px}
.nav{position:absolute;left:178px;top:21px;display:flex;gap:14px;font-size:5.6px;font-weight:600;letter-spacing:.3px;text-transform:uppercase}
.btn{position:absolute;display:flex;align-items:center;justify-content:center;border-radius:12px;font-weight:600;text-transform:uppercase;letter-spacing:.3px;color:var(--white)}
.btn--nav{left:469px;top:16px;width:70px;height:16px;background:var(--orange);font-size:5.6px}
.hero__title{left:43px;top:116px;width:240px;font-size:17px;line-height:21px;font-weight:700}
.hero__lede{left:43px;top:164px;width:170px;font-size:7.5px;line-height:12px}
.btn--hero{left:43px;top:198px;width:86px;height:15px;background:var(--orange);font-size:5.6px}
.hero__art{left:275px;top:95px;width:273px;height:130px;border-radius:14px;background:linear-gradient(135deg,rgba(255,255,255,.28),rgba(244,124,63,.35))}

/* features */
.h-section{position:absolute;left:0;width:582px;text-align:center;font-size:17px;font-weight:500;color:var(--ink)}
.features__title{top:365px}
.feature{position:absolute;top:408px;width:160px}
.feature__art{width:62px;height:45px;border-radius:8px;background:linear-gradient(135deg,#dff1ee,#cfe9e5)}
.feature__name{margin-top:12px;font-size:8px;font-weight:500;color:var(--teal)}
.feature__text{margin-top:5px;font-family:"Montserrat",sans-serif;font-size:6px;line-height:10px;color:var(--muted)}

/* why */
.why__title{left:43px;top:595px;font-size:17px;font-weight:500}
.why__lede{left:43px;top:622px;width:275px;font-size:7px;line-height:11px;color:var(--muted)}
.why__ask{left:43px;top:665px;font-size:10px;font-weight:500}
.point{position:absolute;left:43px;width:220px}
.point__num{position:absolute;left:0;top:2px;width:16px;height:16px;border-radius:50%;background:var(--teal);color:var(--white);font-size:7px;font-weight:600;display:flex;align-items:center;justify-content:center}
.point__name{position:absolute;left:25px;top:0;font-size:9.5px;font-weight:500;color:var(--teal)}
.point__text{position:absolute;left:27px;top:16px;width:185px;font-size:6.3px;line-height:10px;color:var(--muted)}
.why__device{left:330px;top:545px;width:200px;height:325px;border-radius:16px;background:linear-gradient(160deg,#2a2c31 0%,#3a3d44 55%,#e8c6ad 100%)}

/* testimonials */
.voices{top:870px;height:375px;background:var(--mist)}
.voices__title{top:55px}
.voice{position:absolute;top:93px;width:158px}
.voice__video{position:relative;height:89px;background:linear-gradient(160deg,#4a4f57,#8b8f96)}
.voice__caption{position:absolute;left:6px;top:7px;display:flex;align-items:center;gap:4px;font-size:6px;color:var(--white)}
.voice__dot{width:11px;height:11px;border-radius:50%;background:var(--teal)}
.voice__play{position:absolute;left:69px;top:38px;width:20px;height:13px;border-radius:3px;background:#111}
.voice__play::after{content:"";position:absolute;left:8px;top:3.5px;border-left:5px solid var(--white);border-top:3px solid transparent;border-bottom:3px solid transparent}
.voice__name{margin-top:8px;font-size:7.5px;color:var(--ink)}
.voice__role{font-size:5.5px;color:var(--muted)}
.voice__quote{margin-top:10px;font-family:"Montserrat",sans-serif;font-size:6.2px;line-height:11.5px;color:var(--muted)}

/* band */
.band{top:1245px;height:220px;color:var(--white);text-align:center}
.band__photo{position:absolute;inset:0;background:linear-gradient(90deg,var(--orange-deep),var(--orange) 55%,#f58a4e)}
.band__title{position:absolute;left:0;width:582px;top:58px;font-size:16px;line-height:22px;font-weight:600}
.band__lede{position:absolute;left:121px;width:340px;top:105px;font-size:7px;line-height:12.5px}
.btn--band{left:199px;top:145px;width:184px;height:22px;background:var(--teal);font-size:6px}

/* news */
.news{top:1465px;height:205px}
.news__title{top:55px}
.press{position:absolute;top:100px;width:120px;text-align:center;font-size:13px;font-weight:600;color:var(--press)}
.reviews{position:absolute;top:147px;left:0;width:582px;display:flex;justify-content:center;align-items:center;gap:4px;font-size:6px;color:var(--ink)}
.reviews u{color:var(--ink)}
.reviews__mark{width:7px;height:7px;background:var(--teal);margin-left:3px}
.reviews__name{font-weight:600;font-size:7px}

/* footer */
.footer{top:1670px;height:217px;background:var(--sand)}
.fcol{position:absolute;top:73px}
.fcol__head{font-size:8px;font-weight:500;color:var(--ink);margin-bottom:3px}
.fcol__link{font-size:6.8px;line-height:13px;color:var(--muted)}
.socials{position:absolute;left:465px;top:125px;display:flex;gap:10px}
.socials span{width:13px;height:13px;border-radius:50%;background:var(--teal)}
.legal{position:absolute;left:103px;top:174px;display:flex;align-items:center;gap:8px;font-size:6.3px;color:var(--muted)}
.legal .brand{position:static;color:var(--teal)}
.legal .brand__mark{background:var(--teal)}
.legal u{color:#3c63b0}
.chat{position:absolute;left:533px;top:164px;width:30px;height:30px;border-radius:50%;background:var(--teal);box-shadow:0 2px 6px rgba(0,0,0,.18)}
.chat::after{content:"";position:absolute;left:9px;top:9px;width:12px;height:10px;border-radius:3px;background:var(--white)}
</style>
</head>
<body>
<div class="stage">

  <!-- private tutoring page -->
  <article class="page page--private">
    <header class="section hero">
      <div class="brand"><span class="brand__mark"></span>LingoTrail</div>
      <nav class="nav"><span>How it works</span><span>Teachers</span><span>Testimonials</span><span>Pricing</span><span>About us</span></nav>
      <div class="btn btn--nav">Get started</div>
      <h1 class="abs hero__title">Accelerated learning with online Spanish tutoring</h1>
      <p class="abs hero__lede">Learn fast and effectively with fun and engaging private Spanish classes</p>
      <div class="btn btn--hero">Try a free class</div>
      <div class="abs hero__art" role="img" aria-label="Illustration of students learning around a large computer screen"></div>
    </header>

    <h2 class="h-section features__title">Key Features</h2>
    <div class="feature" style="left:43px"><div class="feature__art" role="img" aria-label="Illustration of a teacher at a desk"></div><div class="feature__name">Expert Teachers</div><p class="feature__text">LingoTrail teachers are trained in the science of teaching Spanish and have worked thousands of hours helping Spanish learners globally.</p></div>
    <div class="feature" style="left:211px"><div class="feature__art" role="img" aria-label="Illustration of a learner with a laptop"></div><div class="feature__name">Dedicated Attention</div><p class="feature__text">Accelerate your learning with one-on-one classes featuring a curriculum that's custom built for your unique needs and interests</p></div>
    <div class="feature" style="left:386px"><div class="feature__art" role="img" aria-label="Illustration of a person with chat bubbles"></div><div class="feature__name">Flexible and Convenient</div><p class="feature__text">Online tutoring allows you to learn whenever, and wherever. Find time to continue learning, even if you have a tight schedule.</p></div>

    <h2 class="abs why__title">Why Private Spanish Tutoring?</h2>
    <p class="abs why__lede">Fast-track your language learning using online Spanish classes with a dedicated teacher. Get an effective curriculum that's built around your specific goals and current level of comprehension.</p>
    <h3 class="abs why__ask">What kinds of classes can you expect?</h3>
    <div class="point" style="top:694px"><span class="point__num">1</span><span class="point__name">Conversational</span><p class="point__text">Want to get ready for conversations in the real world? Lessons on every-day topics can help build your vocabulary in essential areas and help you build more confidence speaking.</p></div>
    <div class="point" style="top:763px"><span class="point__num">2</span><span class="point__name">Grammar</span><p class="point__text">Learn the basics or perfect your grammar for use in personal or professional settings. Our grammar-oriented lessons will build you vocabulary while helping you speak perfectly like a native.</p></div>
    <div class="abs why__device" role="img" aria-label="Hand holding a tablet showing the private Spanish tutoring screen"></div>

    <section class="section voices">
      <h2 class="h-section voices__title">What our students say</h2>
      <div class="voice" style="left:43px"><div class="voice__video" role="img" aria-label="Video thumbnail of a student testimonial"><div class="voice__caption"><span class="voice__dot"></span>Hear what Owen has to ...</div><span class="voice__play"></span></div><div class="voice__name">Owen Hartley</div><div class="voice__role">Learning to socialize</div><p class="voice__quote">"The main things to note are the availability and patience of the teachers. Having them available pretty much on standby, and willing to work with me at my speed, ensured a really got enough practice with each subject to feel comfortable before moving on."</p></div>
      <div class="voice" style="left:212px"><div class="voice__video" role="img" aria-label="Video thumbnail of a student testimonial"><div class="voice__caption"><span class="voice__dot"></span>Hear Why Nadia Loves...</div><span class="voice__play"></span></div><div class="voice__name">Nadia</div><div class="voice__role">Learning for for travel</div><p class="voice__quote">"On our first call, my teacher interviewed me to find out what I needed to learn. They used this to create custom class plans and help me get basic conversational skills down. I love Spanish music so I asked her if we could go over some well known songs to start with. This was super cool and helped me having fun while learning Spanish!"</p></div>
      <div class="voice" style="left:381px"><div class="voice__video" role="img" aria-label="Video thumbnail of a student testimonial"><div class="voice__caption"><span class="voice__dot"></span>Learn Spanish Online: M...</div><span class="voice__play"></span></div><div class="voice__name">Marisol</div><div class="voice__role">Learning for music</div><p class="voice__quote">"As I was traveling solo, I really wanted to be able to at least take care of everyday life stuff in Mexico. My schedule did not allow me to actually go to a course though. LingoTrail was great because I could just hop on pretty much instantly and have a class. This flexibility allowed me to drop the excuse of not having enough time."</p></div>
    </section>

    <section class="section band">
      <div class="band__photo" role="img" aria-label="Photo of a group class with an orange tint"></div>
      <h2 class="band__title">Group classes are also available OR<br>Try group classes instead</h2>
      <p class="band__lede">Led by our certified teachers, group classes give learners the opportunity to have real, interactive conversations in Spanish with their peers.</p>
      <div class="btn btn--band">Learn more about private tutoring</div>
    </section>

    <section class="section news">
      <h2 class="h-section news__title">We've been in the News</h2>
      <div class="press" style="left:38px">Ventura Weekly</div>
      <div class="press" style="left:166px">Ledger Daily</div>
      <div class="press" style="left:296px">Metro Post</div>
      <div class="press" style="left:424px">Market Notes</div>
      <div class="reviews">Check our reviews <u>here</u><span class="reviews__mark"></span><span class="reviews__name">ReviewNest</span></div>
    </section>

    <footer class="section footer">
      <div class="fcol" style="left:43px"><div class="fcol__head">Information</div><div class="fcol__link">How It Works</div><div class="fcol__link">Pricing</div></div>
      <div class="fcol" style="left:146px"><div class="fcol__head">Service</div><div class="fcol__link">Teachers</div><div class="fcol__link">Testimonials</div></div>
      <div class="fcol" style="left:250px"><div class="fcol__head">Company</div><div class="fcol__link">About Us</div><div class="fcol__link">Partner Program</div></div>
      <div class="fcol" style="left:353px"><div class="fcol__head">Legal</div><div class="fcol__link">Privacy policy</div><div class="fcol__link">Terms of use</div></div>
      <div class="fcol" style="left:465px"><div class="fcol__head">Get in touch</div><div class="fcol__link">Contact Support</div></div>
      <div class="socials"><span></span><span></span><span></span></div>
      <div class="legal"><div class="brand"><span class="brand__mark"></span>LingoTrail</div>Copyright © 2020 LingoTrail, Inc. All rights reserved. <u>Privacy Policy</u>. Terms &amp; Conditions.</div>
      <div class="chat"></div>
    </footer>
  </article>

  <!-- group classes page -->
  <article class="page page--group">
    <header class="section hero">
      <div class="brand"><span class="brand__mark"></span>LingoTrail</div>
      <nav class="nav"><span>How it works</span><span>Teachers</span><span>Testimonials</span><span>Pricing</span><span>About us</span></nav>
      <div class="btn btn--nav">Get started</div>
      <h1 class="abs hero__title">Learning is fun with online group Spanish classes</h1>
      <p class="abs hero__lede">Practice together online with real, interactive classes in Spanish</p>
      <div class="btn btn--hero">Try a free class</div>
      <div class="abs hero__art" role="img" aria-label="Illustration of a teacher on a computer screen and a student on books"></div>
    </header>

    <h2 class="h-section features__title">Key Features</h2>
    <div class="feature" style="left:43px"><div class="feature__art" role="img" aria-label="Illustration of a teacher at a desk"></div><div class="feature__name">Expert Teachers</div><p class="feature__text">LingoTrail teachers are experts at bringing students together in our group classes, so you can collaborate and improve together</p></div>
    <div class="feature" style="left:211px"><div class="feature__art" role="img" aria-label="Illustration of a learner with a laptop"></div><div class="feature__name">Engaging Lessons</div><p class="feature__text">Pick and choose the classes you want to take by your unique needs and interests. Every class includes fun group activities</p></div>
    <div class="feature" style="left:386px"><div class="feature__art" role="img" aria-label="Illustration of a person with chat bubbles"></div><div class="feature__name">Unlimited Classes</div><p class="feature__text">Take as many classes as you'd like. Lock in your spot by scheduling in advance or drop into classes last minute</p></div>

    <h2 class="abs why__title">Why online Spanish classes?</h2>
    <p class="abs why__lede" style="width:200px">Taking classes in a group settings allows you to What kinds of classes can you expect?</p>
    <div class="point" style="top:665px"><span class="point__num">1</span><span class="point__name">Conversational</span><p class="point__text">Want to get ready for conversations in the real world? Lessons on every-day topics can help build your vocabulary in essential areas and help you build more confidence speaking.</p></div>
    <div class="point" style="top:734px"><span class="point__num">2</span><span class="point__name">Grammar</span><p class="point__text">Learn the basics or perfect your grammar for use in personal or professional settings. Our grammar-oriented lessons will build you vocabulary while helping you speak perfectly like a native.</p></div>
    <div class="abs why__device" role="img" aria-label="Hand holding a tablet showing the Spanish group classes screen"></div>

    <section class="section voices">
      <h2 class="h-section voices__title">What our students say</h2>
      <div class="voice" style="left:43px"><div class="voice__video" role="img" aria-label="Video thumbnail of a student testimonial"><div class="voice__caption"><span class="voice__dot"></span>Hear what Owen has to ...</div><span class="voice__play"></span></div><div class="voice__name">Owen Hartley</div><div class="voice__role">Learning to socialize</div><p class="voice__quote">"The main things to note are the availability and patience of the teachers. Having them available pretty much on standby, and willing to work with me at my speed, ensured a really got enough practice with each subject to feel comfortable before moving on."</p></div>
      <div class="voice" style="left:212px"><div class="voice__video" role="img" aria-label="Video thumbnail of a student testimonial"><div class="voice__caption"><span class="voice__dot"></span>Hear Why Nadia Loves...</div><span class="voice__play"></span></div><div class="voice__name">Nadia</div><div class="voice__role">Learning for for travel</div><p class="voice__quote">"On our first call, my teacher interviewed me to find out what I needed to learn. They used this to create custom class plans and help me get basic conversational skills down. I love Spanish music so I asked her if we could go over some well known songs to start with. This was super cool and helped me having fun while learning Spanish!"</p></div>
      <div class="voice" style="left:381px"><div class="voice__video" role="img" aria-label="Video thumbnail of a student testimonial"><div class="voice__caption"><span class="voice__dot"></span>Learn Spanish Online: M...</div><span class="voice__play"></span></div><div class="voice__name">Marisol</div><div class="voice__role">Learning for music</div><p class="voice__quote">"As I was traveling solo, I really wanted to be able to at least take care of everyday life stuff in Mexico. My schedule did not allow me to actually go to a course though. LingoTrail was great because I could just hop on pretty much instantly and have a class. This flexibility allowed me to drop the excuse of not having enough time."</p></div>
    </section>

    <section class="section band">
      <div class="band__photo" role="img" aria-label="Photo of a young learner studying with an orange tint"></div>
      <h2 class="band__title">Private tutoring is also available OR<br>Try private tutoring instead</h2>
      <p class="band__lede">Led by our certified teachers, group classes give learners the opportunity to have real, interactive conversations in Spanish with their peers.</p>
      <div class="btn btn--band">Learn more about private tutoring</div>
    </section>

    <section class="section news">
      <h2 class="h-section news__title">We've been in the News</h2>
      <div class="press" style="left:38px">Ventura Weekly</div>
      <div class="press" style="left:166px">Ledger Daily</div>
      <div class="press" style="left:296px">Metro Post</div>
      <div class="press" style="left:424px">Market Notes</div>
      <div class="reviews">Check our reviews <u>here</u><span class="reviews__mark"></span><span class="reviews__name">ReviewNest</span></div>
    </section>

    <footer class="section footer">
      <div class="fcol" style="left:43px"><div class="fcol__head">Information</div><div class="fcol__link">How It Works</div><div class="fcol__link">Pricing</div></div>
      <div class="fcol" style="left:146px"><div class="fcol__head">Service</div><div class="fcol__link">Teachers</div><div class="fcol__link">Testimonials</div></div>
      <div class="fcol" style="left:250px"><div class="fcol__head">Company</div><div class="fcol__link">About Us</div><div class="fcol__link">Partner Program</div></div>
      <div class="fcol" style="left:353px"><div class="fcol__head">Legal</div><div class="fcol__link">Privacy policy</div><div class="fcol__link">Terms of use</div></div>
      <div class="fcol" style="left:465px"><div class="fcol__head">Get in touch</div><div class="fcol__link">Contact Support</div></div>
      <div class="socials"><span></span><span></span><span></span></div>
      <div class="legal"><div class="brand"><span class="brand__mark"></span>LingoTrail</div>Copyright © 2020 LingoTrail, Inc. All rights reserved. <u>Privacy Policy</u>. Terms &amp; Conditions.</div>
      <div class="chat"></div>
    </footer>
  </article>

</div>
</body>
</html>
```